Harlowe plumbing business cards

Want a functional designed for my business cards using my logo

Company Name- Harlowe Plumbing, Heating & Water Systems
Name- Marcus Harlowe
Title- Vice President
Cell- 555-318-7426
Email- Harloweplumbing@mailbrook.net
Business address-
PO Box 37
Fenwick Mill, MD 21999

Industry/Entity Type

Plumbing

```html
<!DOCTYPE html>
<html lang="en">
<head>
<meta charset="utf-8">
<title>Harlowe Plumbing Business Cards</title>
<link rel="stylesheet" href="https://fonts.googleapis.com/css2?family=Open+Sans:wght@400;600&family=Arimo:wght@400;700&display=swap">
<style>
  :root {
    --backdrop: #2b2b2b;
    --card: #1c1c1d;
    --card-edge: #262628;
    --brand-blue: #1e78d2;
    --text-white: #f2f2f2;
    --muted-white: #d9d9d9;
  }
  * { box-sizing: border-box; margin: 0; padding: 0; }
  html, body {
    width: 1200px; height: 1189px; overflow: hidden;
    background: var(--backdrop);
  }
  .sheet {
    position: relative; width: 1200px; height: 1189px;
    display: flex; flex-direction: column; align-items: center;
    justify-content: center; gap: 60px;
  }
  .card {
    position: relative; width: 860px; height: 491px;
    background: var(--card);
    border-radius: 28px;
    border: 1px solid var(--card-edge);
    box-shadow: 0 18px 40px rgba(0,0,0,0.45);
    color: var(--text-white);
  }
  .brand-block {
    position: absolute; text-align: center;
    font-family: "Open Sans", sans-serif;
  }
  .card--front .brand-block { left: 0; right: 0; top: 150px; }
  .card--back .brand-block { right: 50px; top: 150px; width: 380px; }
  .brand-name {
    display: flex; align-items: center; justify-content: center; gap: 14px;
    font-size: 46px; font-weight: 400; color: var(--brand-blue);
    line-height: 1.1;
  }
  .brand-dot {
    width: 20px; height: 20px; border-radius: 50%;
    background: var(--brand-blue);
  }
  .brand-tagline {
    margin-top: 6px; font-size: 25px; color: var(--text-white);
    letter-spacing: 0.3px;
  }
  .brand-phone {
    margin-top: 22px; font-size: 40px; color: var(--brand-blue);
    letter-spacing: 0.5px;
  }
  .contact {
    position: absolute; left: 60px; top: 150px;
    font-family: "Arimo", sans-serif; font-size: 21px; line-height: 1.3;
  }
  .contact-name { color: var(--brand-blue); font-weight: 700; font-size: 26px; }
  .contact-title { color: var(--text-white); font-size: 22px; }
  .contact-address { margin-top: 26px; color: var(--text-white); }
  .contact-line {
    display: flex; align-items: center; gap: 12px; margin-top: 8px;
  }
  .contact-address + .contact-line { margin-top: 14px; }
  .contact-icon { width: 28px; height: 28px; flex: none; }
  .contact-web {
    margin-top: 30px; letter-spacing: 5px; font-size: 20px;
    color: var(--muted-white);
  }
  .contact-web .web-domain { color: var(--brand-blue); }
</style>
</head>
<body>
<main class="sheet">

  <section class="card card--front" aria-label="Card front">
    <div class="brand-block">
      <div class="brand-name"><span class="brand-dot"></span>Harlowe Plumbing</div>
      <div class="brand-tagline">Heating &amp; Water Systems</div>
      <div class="brand-phone">555.204.8193</div>
    </div>
  </section>

  <section class="card card--back" aria-label="Card back">
    <div class="contact">
      <div class="contact-name">Marcus Harlowe</div>
      <div class="contact-title">Vice President</div>
      <div class="contact-address">PO Box 37<br>Fenwick Mill, MD 21999</div>
      <div class="contact-line">
        <svg class="contact-icon" viewBox="0 0 28 28" aria-hidden="true">
          <circle cx="14" cy="14" r="12.5" fill="none" stroke="var(--brand-blue)" stroke-width="1.8"/>
          <rect x="10" y="7.5" width="8" height="13" rx="1.5" fill="none" stroke="var(--brand-blue)" stroke-width="1.6"/>
          <line x1="12.5" y1="18" x2="15.5" y2="18" stroke="var(--brand-blue)" stroke-width="1.4"/>
        </svg>
        <span>555-318-7426</span>
      </div>
      <div class="contact-line">
        <svg class="contact-icon" viewBox="0 0 28 28" aria-hidden="true">
          <circle cx="14" cy="14" r="12.5" fill="none" stroke="var(--brand-blue)" stroke-width="1.8"/>
          <rect x="7.5" y="9.5" width="13" height="9" fill="var(--brand-blue)"/>
          <polyline points="7.5,9.5 14,15 20.5,9.5" fill="none" stroke="var(--card)" stroke-width="1.4"/>
        </svg>
        <span>Harloweplumbing@mailbrook.net</span>
      </div>
      <div class="contact-web">www.<span class="web-domain">harloweplumbing</span>.net</div>
    </div>
    <div class="brand-block">
      <div class="brand-name"><span class="brand-dot"></span>Harlowe Plumbing</div>
      <div class="brand-tagline">Heating &amp; Water Systems</div>
      <div class="brand-phone">555.204.8193</div>
    </div>
  </section>

</main>
</body>
</html>
```